We are looking for a poster / flyer to advertise our Squash Tournament - the Wrenfold Club Sydney CBD Squash Open. I have provided the details and sponsor logos that need to appear on the poster in the attachments.
I am open to the poster including pictures of real life squash playing action shots or a complete graphic art design.

Target Market(s)

Squash Players and Sporty People who may be interested in trying Squash as a new Sport

Requirements
Must have
• 1. All logos attached in files (logos in the word doc and the Bramwick Logo)
2. Content that has been provided in the word doc
3. Printable on A3 paper
4. Title of the poster must be 2021 Wrenfold Club Sydney CBD Squash Open
Nice to have
• 1.Design must be related to the Sport of Squash (can either be a graphic Design that incorporates a real life squash pic rom the internet or 100% graphic)
2. Something incorporating both female and junior squash player participation.
3. Poster depicts action / athleticism.

```html
<!DOCTYPE html>
<html lang="en">
<head>
<meta charset="utf-8">
<title>2021 Wrenfold Club Sydney CBD Squash Open</title>
<link href="https://fonts.googleapis.com/css2?family=Bebas+Neue&family=Big+Shoulders+Stencil+Display:wght@900&family=Saira+Stencil+One&family=Oswald:wght@400;500&family=PT+Sans:ital,wght@0,400;1,400&display=swap" rel="stylesheet">
<style>
  :root {
    --navy: #141a33;
    --navy-deep: #0c1024;
    --gold: #f3b52c;
    --white: #ffffff;
    --stone: #c9c9c9;
    --muted: #b8bccb;
  }
  * { margin: 0; padding: 0; box-sizing: border-box; }
  html, body { width: 946px; height: 1200px; overflow: hidden; background: var(--navy-deep); }
  .poster {
    position: relative; width: 946px; height: 1200px; overflow: hidden;
    background: linear-gradient(180deg, #1c2442 0%, var(--navy) 45%, var(--navy-deep) 100%);
    color: var(--white);
    font-family: "Oswald", sans-serif;
  }
  .stripes { position: absolute; inset: 0; }
  .player-photo {
    position: absolute; left: 410px; top: 0; width: 536px; height: 820px;
    background: radial-gradient(ellipse at 62% 35%, #9a9a9a 0%, #5e5e62 40%, rgba(30,34,52,0) 75%);
  }
  .event-title {
    position: absolute; left: 44px; top: 62px;
    font-family: "Bebas Neue", sans-serif; font-weight: 400;
    font-size: 50px; line-height: 58px; color: var(--gold);
  }
  .rule { position: absolute; left: 60px; width: 820px; height: 3px; background: var(--gold); }
  .rule.top { top: 452px; }
  .rule.info-top { top: 820px; }
  .rule.info-bottom { top: 873px; }
  .rule.footer { top: 1117px; height: 2px; }
  .headline-art { position: absolute; left: 0; top: 0; width: 946px; height: 820px; overflow: visible; }
  .headline-main {
    font-family: "Saira Stencil One", sans-serif; font-size: 250px;
    fill: var(--stone); stroke: var(--gold); stroke-width: 5px; paint-order: stroke fill;
  }
  .headline-sub {
    font-family: "Big Shoulders Stencil Display", sans-serif; font-weight: 900; font-size: 128px;
    fill: var(--white); filter: drop-shadow(0 6px 8px rgba(0,0,0,.6));
  }
  .info-bar { position: absolute; left: 60px; top: 823px; width: 820px; height: 50px; display: flex; align-items: center; }
  .info-bar .dates { width: 216px; font-family: "Bebas Neue", sans-serif; font-size: 34px; padding-left: 6px; }
  .info-bar .cell { font-size: 13px; line-height: 16px; text-transform: uppercase; padding: 0 14px; border-left: 2px solid var(--gold); height: 40px; display: flex; align-items: center; }
  .info-bar .venue { width: 370px; }
  .info-bar .finals { width: 234px; padding-left: 40px; }
  .grades { position: absolute; left: 62px; top: 912px; }
  .grades h2 { font-family: "Bebas Neue", sans-serif; font-weight: 400; font-size: 27px; color: var(--gold); margin-bottom: 4px; }
  .grades ul { list-style: none; }
  .grades li { display: flex; align-items: center; gap: 12px; font-size: 15px; line-height: 24px; text-transform: uppercase; }
  .grades svg { width: 16px; height: 12px; flex: none; }
  .details { position: absolute; left: 497px; top: 914px; width: 300px; font-family: "PT Sans", sans-serif; font-size: 13px; line-height: 16px; }
  .details .note { font-style: italic; margin-bottom: 12px; }
  .details .deadline { font-family: "Oswald", sans-serif; color: var(--gold); text-transform: uppercase; font-size: 14px; margin: 14px 0 6px; }
  .uni-mark { position: absolute; left: 770px; top: 1040px; display: flex; align-items: center; gap: 8px; font-size: 17px; font-weight: 500; color: var(--gold); }
  .mark-circle { width: 26px; height: 26px; border-radius: 50%; background: var(--gold); flex: none; }
  .sponsors { position: absolute; left: 60px; top: 1138px; width: 826px; height: 52px; display: flex; align-items: center; justify-content: space-between; }
  .badge { width: 52px; height: 52px; border-radius: 50%; background: #2a2f48; border: 2px solid #b78a2a; }
  .badge.small { width: 36px; height: 40px; border-radius: 6px; background: var(--muted); border: none; }
  .sponsor-name { font-size: 24px; font-weight: 500; color: var(--white); text-transform: uppercase; letter-spacing: 1px; }
</style>
</head>
<body>
<main class="poster">
  <svg class="stripes" width="946" height="1200" viewBox="0 0 946 1200" aria-hidden="true">
    <polygon points="0,0 90,0 0,190" fill="var(--gold)" opacity=".9"/>
    <polygon points="800,0 860,0 440,470 380,470" fill="var(--gold)"/>
    <polygon points="946,220 946,290 690,560 620,560" fill="var(--gold)"/>
    <line x1="540" y1="300" x2="360" y2="500" stroke="var(--gold)" stroke-width="3"/>
    <line x1="555" y1="300" x2="375" y2="500" stroke="var(--gold)" stroke-width="3"/>
  </svg>
  <div class="player-photo" role="img" aria-label="Black and white action photo of a female squash player lunging with her racket"></div>

  <h1 class="event-title">2021 Wrenfold Club<br>Sydney CBD Squash Open</h1>

  <div class="rule top"></div>
  <svg class="headline-art" width="946" height="820" viewBox="0 0 946 820" role="img" aria-label="Squash Tournament">
    <text class="headline-main" x="64" y="648" textLength="818" lengthAdjust="spacingAndGlyphs">SQUASH</text>
    <text class="headline-sub" x="64" y="792" textLength="818" lengthAdjust="spacingAndGlyphs">TOURNAMENT</text>
  </svg>

  <div class="rule info-top"></div>
  <div class="info-bar">
    <div class="dates">13 TH – 15TH AUG.</div>
    <div class="cell venue">Held at CBD courts (Wrenfold &amp; Harcourt Clubs)<br>and Ridgeway Uni. Sports &amp; Fitness</div>
    <div class="cell finals">All finals will be at the<br>Wrenfold Club</div>
  </div>
  <div class="rule info-bottom"></div>

  <section class="grades">
    <h2>Grades available:</h2>
    <ul>
      <li><svg viewBox="0 0 16 12"><path d="M1 6l5 5L15 1" fill="none" stroke="var(--gold)" stroke-width="2.5"/></svg>Mens and ladies squash open, $14K in prizemoney</li>
      <li><svg viewBox="0 0 16 12"><path d="M1 6l5 5L15 1" fill="none" stroke="var(--gold)" stroke-width="2.5"/></svg>Racquetball open</li>
      <li><svg viewBox="0 0 16 12"><path d="M1 6l5 5L15 1" fill="none" stroke="var(--gold)" stroke-width="2.5"/></svg>Junior events</li>
      <li><svg viewBox="0 0 16 12"><path d="M1 6l5 5L15 1" fill="none" stroke="var(--gold)" stroke-width="2.5"/></svg>All grades / abilities catered for</li>
      <li><svg viewBox="0 0 16 12"><path d="M1 6l5 5L15 1" fill="none" stroke="var(--gold)" stroke-width="2.5"/></svg>Players guaranteed 3 matches</li>
      <li><svg viewBox="0 0 16 12"><path d="M1 6l5 5L15 1" fill="none" stroke="var(--gold)" stroke-width="2.5"/></svg>$60 entry fee</li>
    </ul>
  </section>

  <section class="details">
    <p class="note">Saturday Night Open Bar in CBD provided by Sponsor ($3K bar tab)</p>
    <p class="note">Weekday matches also organised for CBD workers preferring to play during the day</p>
    <p class="deadline">Entries close 7th August 2021</p>
    <p>Tournament Director<br>Contact: Daniel Ashcombe<br>daniel.ashcombe@example.com<br>0491570156</p>
  </section>

  <div class="uni-mark"><span class="mark-circle"></span>Ridgeway Uni</div>

  <div class="rule footer"></div>
  <footer class="sponsors">
    <span class="badge"></span>
    <span class="badge small"></span>
    <span class="sponsor-name">Harcourt</span>
    <span class="badge"></span>
    <span class="sponsor-name">Bramwick</span>
    <span class="sponsor-name">Wrenfold Club</span>
  </footer>
</main>
</body>
</html>
```